HR Outsourcing and Payroll Company needs a website re-design

The client is LarkfieldHR: www .larkfield-hr. example

They provide services to other businesses, specifically Human Resources (HR) Outsourcing and Payroll services. They are not happy with their current website and have retained our agency to provide a re-design.

You will design 4 pages for us to show the client. They will select a design they like. My agency will take the winning design and files and design the remaining pages of the site. But, we need you to help us establish a design for the basics so they can select a direction.

We need a Homepage design, a Service Page design, a Broker page design, and a Contact page design.

They really like these websites (in order from most preferred look and feel of imagery and design elements), so I think a mix between the two would be great:

https://www.brisvane.example/
http://www.quelmora.example/

I have attached a project brief for this website. Please refer to it... It will help you be successful in what you deliver. The best designs will incorporate functionality and elements from the project brief.

Target Market(s)

Business owners. They will be thinking about thinks like employee reviews, payroll, time keeping, hiring, being compliant with state laws, and needing an expert to help them.

Industry/Entity Type

It Company

Number of Pages Required

4 page

Font styles to use
Sans Serif

Colors
f37122
0255a3
fbed22
9bcb3c
ec1f27

Requirements
Must have
• We need:
• -Homepage design (desktop and mobile)
• -Service Page design (desktop and mobile)
• -Broker page design (desktop and mobile)
• -Contact page design (desktop and mobile)
• Inspiration: a mix between the two would be great:
• https://www.brisvane.example/
• http://www.quelmora.example/
• They like the long extended homepage look:
• http://www.quelmora.example/
• Photos that have focused people in the front and blurred backgrounds. Example: https://www.brisvane.example/
• Graphic Icons for their services. Example:
• http://www.quelmora.example/
• I have attached a project brief for this website. Please refer to it... It will help you be successful in what you deliver. The best designs will incorporate functionality and elements from the project brief.
Should not have
• Crappy stock photos... you can use watermarked stock photos if you don't wish to purchase them for the sake of the contest.

```html
<!DOCTYPE html>
<html lang="en">
<head>
<meta charset="utf-8">
<title>LarkfieldHR – HR Outsourcing &amp; Payroll</title>
<link rel="stylesheet" href="https://fonts.googleapis.com/css2?family=Open+Sans:wght@400;600;700&display=swap">
<style>
:root{
  --blue:#2468b0;
  --blue-dark:#1b4f91;
  --blue-nav:#1d5aa6;
  --gold:#c48a3e;
  --gold-dark:#a8742f;
  --ink:#333;
  --muted:#777;
  --light:#f2f2f2;
  --footer:#5b5b5b;
  --white:#fff;
}
*{box-sizing:border-box;margin:0;padding:0}
html,body{width:1200px;height:4390px;overflow:hidden}
body{font-family:"Open Sans",Arial,sans-serif;color:var(--ink);background:var(--white)}
section,header,nav,footer{position:relative;width:1200px;overflow:hidden}
.abs{position:absolute}
.center{text-align:center;left:0;width:1200px}
.section-title{font-size:38px;font-weight:400;letter-spacing:.5px}
.t-blue{color:var(--blue)}
.t-gold{color:var(--gold)}
.lead{font-size:13px;color:var(--muted);line-height:1.7}
.more{color:var(--gold);font-size:12px;text-decoration:underline}

/* header */
.site-header{height:123px;background:var(--white)}
.social-dot{width:18px;height:18px;border-radius:50%;background:var(--blue);top:11px}
.search{left:878px;top:6px;width:214px;height:30px;border:1px solid #ccc;font-size:12px;color:#999;padding:6px 10px}
.search-btn{left:1092px;top:6px;width:30px;height:30px;background:var(--gold)}
.brand{font-size:34px;font-weight:700;color:var(--blue);top:55px;left:79px}
.call{left:767px;top:68px;font-size:22px;color:var(--blue)}
.call-icon{left:920px;top:64px;width:40px;height:40px;border-radius:50%;border:2px solid var(--blue)}
.call-num{left:975px;top:66px;font-size:24px;font-weight:700;color:var(--blue)}

/* nav */
.main-nav{height:58px;background:var(--gold)}
.main-nav a{position:absolute;top:0;height:58px;line-height:58px;color:var(--white);font-size:15px;text-decoration:none;padding:0 28px}
.main-nav a.active{background:var(--blue-nav)}

/* hero */
.hero{height:574px;background:linear-gradient(100deg,#d9dee4 0%,#c8d2dc 35%,#9fb0c2 65%,#6f8296 100%)}
.hero-title{left:79px;top:132px;width:360px;height:56px;background:rgba(40,40,40,.55);color:var(--white);font-size:44px;font-weight:700;padding-left:10px;line-height:56px}
.hero-sub{left:79px;top:212px;width:360px;height:34px;background:rgba(40,40,40,.5);color:var(--white);font-size:19px;padding-left:10px;line-height:34px}
.btn-pill{display:inline-block;border-radius:26px;font-weight:700;text-align:center}
.hero-btn{left:79px;top:264px;width:199px;height:52px;line-height:52px;background:var(--blue-nav);color:var(--white);font-size:14px}
.stats{left:0;top:449px;width:1200px;height:125px;background:rgba(255,255,255,.82)}
.stat{top:20px;width:280px;text-align:center}
.stat b{display:block;font-size:32px;font-weight:400;color:#222}
.stat span{font-size:14px;color:#555}
.arrow-sq{top:64px;width:34px;height:40px;background:var(--blue-nav)}

/* services */
.services{height:430px}
.svc{top:123px;width:187px;height:258px;border-top:3px solid var(--gold);box-shadow:0 1px 6px rgba(0,0,0,.18);background:var(--white);text-align:center;padding:24px 14px}
.svc svg{width:62px;height:62px}
.svc h3{color:var(--gold);font-size:19px;font-weight:400;line-height:1.2;margin:14px 0 10px}
.svc p{font-size:12.5px;color:#555;line-height:1.6}

/* welcome */
.welcome{height:372px;background:var(--blue)}
.welcome-photo{left:0;top:0;width:463px;height:372px;background:linear-gradient(120deg,#e9e6e2,#b9b4ad 55%,#7d7a78)}
.welcome-text{left:463px;top:0;width:737px;height:372px;background:linear-gradient(90deg,#2a6eb5,#1e5ca0)}
.welcome h2{position:absolute;left:55px;top:50px;font-size:38px;font-weight:400;color:var(--white)}
.welcome p{position:absolute;left:55px;top:118px;width:620px;font-size:14px;line-height:1.75;color:#e5eefa}
.welcome .btn-pill{position:absolute;left:55px;top:276px;width:170px;height:46px;line-height:46px;background:var(--white);color:var(--blue);font-size:14px}

/* broker */
.broker{height:580px}
.broker-card{top:214px;width:322px;text-align:center}
.ph{height:184px}
.broker-card h3{color:var(--gold);font-size:20px;font-weight:400;margin:14px 0 8px}
.broker-card p{font-size:13px;color:#555;line-height:1.7}

/* trust */
.trust{height:298px;background:var(--light)}
.trust-logo{top:192px;width:240px;text-align:center;font-size:30px;font-weight:700;color:var(--blue)}

/* resources */
.resources{height:527px;background:linear-gradient(135deg,#c99a55,#b07d3b 50%,#a06c2c)}
.res{top:214px;width:234px;text-align:center;color:var(--white)}
.res .ph{height:134px}
.res h3{font-size:19px;font-weight:700;margin:14px 0 6px}
.res p{font-size:13px;line-height:1.6;color:#f8efe1}
.res .more{color:var(--white)}

/* blog */
.blog{height:331px}
.post-img{top:140px;width:206px;height:138px}
.post{top:140px;width:260px}
.post h4{color:var(--blue);font-size:14px;font-weight:400}
.post .date{font-size:13px;color:#555;margin:6px 0 10px}
.post p{font-size:13px;color:#555;line-height:1.6}

/* testimonials */
.testimonials{height:410px;background:linear-gradient(90deg,#2b6fb6,#2566ac 60%,#3a7cc0)}
.quote-mark{left:575px;top:115px;width:50px;height:50px;border-radius:50%;border:2px solid var(--white);color:var(--white);font-size:36px;text-align:center;line-height:54px;font-weight:700}
.t-text{left:160px;top:190px;width:880px;text-align:center;font-size:14px;line-height:1.75;color:var(--white)}
.avatar{left:490px;top:290px;width:74px;height:74px;border-radius:50%;background:#c7d3df;border:3px solid var(--white)}
.client{left:594px;top:316px;color:var(--white);font-size:15px}
.circle-arrow{top:195px;width:36px;height:36px;border-radius:50%;border:2px solid var(--white)}

/* contact */
.contact{height:366px}
.field{height:50px;width:370px;border:1px solid #d5d5d5;font-size:13px;color:#999;padding:15px 16px}
.submit{left:614px;top:258px;width:370px;height:52px;background:var(--gold);color:var(--white);font-size:19px;font-weight:700;text-align:center;line-height:52px}

/* footer */
.site-footer{height:278px;background:var(--footer);color:var(--white)}
.site-footer h5{font-size:18px;font-weight:400;position:absolute;top:24px}
.links{left:351px;top:76px;font-size:14px;line-height:26px}
.foot-input{left:620px;width:232px;height:40px;background:var(--white);color:#333;font-size:13px;padding:10px 8px}
.subscribe{left:620px;top:222px;width:144px;height:40px;background:var(--white);color:var(--blue);font-size:14px;text-align:center;line-height:40px;font-weight:600}
.contact-line{left:916px;font-size:14px;line-height:22px;width:230px}
.foot-social{top:183px;width:56px;height:56px;border-radius:50%;background:var(--blue-nav)}
.bottom-bar{height:43px;background:var(--gold);color:var(--white);font-size:14px}
</style>
</head>
<body>

<header class="site-header">
  <span class="abs social-dot" style="left:68px"></span>
  <span class="abs social-dot" style="left:112px"></span>
  <span class="abs social-dot" style="left:156px"></span>
  <span class="abs social-dot" style="left:198px"></span>
  <div class="abs search">Search here...</div>
  <div class="abs search-btn">
    <svg width="30" height="30" viewBox="0 0 30 30"><circle cx="14" cy="14" r="6" fill="none" stroke="#fff" stroke-width="2"/><line x1="18" y1="18" x2="23" y2="23" stroke="#fff" stroke-width="2"/></svg>
  </div>
  <div class="abs brand">LarkfieldHR</div>
  <div class="abs call">Call us now</div>
  <div class="abs call-icon">
    <svg width="36" height="36" viewBox="0 0 36 36"><path d="M12 10c2 0 3 4 2 5l-2 1c1 3 4 6 7 7l1-2c1-1 5 0 5 2l-1 3c-8 1-16-7-15-15z" fill="#2468b0"/></svg>
  </div>
  <div class="abs call-num">123 456 7890</div>
</header>

<nav class="main-nav">
  <a class="active" style="left:79px">HOME</a>
  <a style="left:206px">ABOUT</a>
  <a style="left:341px">SERVICES</a>
  <a style="left:502px">BROKER</a>
  <a style="left:645px">RESOURCES</a>
  <a style="left:824px">BLOG</a>
  <a style="left:944px">CONTACT</a>
</nav>

<section class="hero" role="img" aria-label="Smiling business professional at a desk with colleagues blurred behind">
  <div class="abs hero-title">LARKFIELDHR</div>
  <div class="abs hero-sub">Get Your FREE HR Assessment</div>
  <div class="abs btn-pill hero-btn">CONTACT US NOW</div>
  <div class="abs stats">
    <div class="abs stat" style="left:27px"><b>94,000</b><span>Employers nationwide</span></div>
    <div class="abs stat" style="left:308px"><b>13,000+</b><span>SMB customers</span></div>
    <div class="abs stat" style="left:577px"><b>25</b><span>Years in business</span></div>
    <div class="abs stat" style="left:905px"><b>$31 Billion+</b><span>Payroll managed annually</span></div>
    <div class="abs arrow-sq" style="left:0"><svg width="34" height="40"><path d="M20 13l-7 7 7 7" fill="none" stroke="#fff" stroke-width="2.5"/></svg></div>
    <div class="abs arrow-sq" style="left:1166px"><svg width="34" height="40"><path d="M14 13l7 7-7 7" fill="none" stroke="#fff" stroke-width="2.5"/></svg></div>
  </div>
</section>

<section class="services">
  <h2 class="abs center section-title" style="top:52px"><span class="t-blue">OUR</span> <span class="t-gold">SERVICES</span></h2>
  <div class="abs svc" style="left:79px">
    <svg viewBox="0 0 62 62"><circle cx="22" cy="20" r="8" fill="#2468b0"/><path d="M8 44c0-10 6-15 14-15s14 5 14 15z" fill="#2468b0"/><circle cx="40" cy="30" r="11" fill="none" stroke="#2468b0" stroke-width="4"/><line x1="48" y1="38" x2="57" y2="48" stroke="#2468b0" stroke-width="5"/></svg>
    <h3>HR Outsourcing</h3>
    <p>Lorem Ipsum is simply dummy text of the print ing and... <span class="more">READ MORE</span></p>
  </div>
  <div class="abs svc" style="left:292px">
    <svg viewBox="0 0 62 62"><path d="M31 6l20 7v16c0 14-9 23-20 27C20 52 11 43 11 29V13z" fill="none" stroke="#2468b0" stroke-width="4"/><rect x="24" y="28" width="14" height="12" fill="#2468b0"/><path d="M27 28v-4a4 4 0 0 1 8 0v4" fill="none" stroke="#2468b0" stroke-width="3"/></svg>
    <h3>Safety</h3>
    <p>Lorem Ipsum is simply dummy text of the print ing and... <span class="more">READ MORE</span></p>
  </div>
  <div class="abs svc" style="left:506px">
    <svg viewBox="0 0 62 62"><circle cx="24" cy="18" r="9" fill="#2468b0"/><path d="M8 54c0-14 7-22 16-22s16 8 16 22z" fill="#2468b0"/><circle cx="46" cy="40" r="11" fill="#fff" stroke="#2468b0" stroke-width="3"/><text x="46" y="46" font-size="16" text-anchor="middle" fill="#2468b0" font-family="Arial" font-weight="700">$</text></svg>
    <h3>Payroll /<br>Timekeeping</h3>
    <p>Lorem Ipsum is simply dummy... <span class="more">READ MORE</span></p>
  </div>
  <div class="abs svc" style="left:720px">
    <svg viewBox="0 0 62 62"><rect x="10" y="10" width="34" height="44" rx="3" fill="none" stroke="#2468b0" stroke-width="4"/><rect x="20" y="6" width="14" height="8" fill="#2468b0"/><path d="M16 32h8l4-8 6 14 4-6h16" fill="none" stroke="#2468b0" stroke-width="3"/></svg>
    <h3>Benefits<br>Administration</h3>
    <p>Lorem Ipsum is simply dummy... <span class="more">READ MORE</span></p>
  </div>
  <div class="abs svc" style="left:934px">
    <svg viewBox="0 0 62 62"><path d="M24 8h14l-4 8h-6z" fill="#2468b0"/><path d="M26 18h10c10 6 16 16 16 26 0 8-6 12-21 12S10 52 10 44c0-10 6-20 16-26z" fill="#2468b0"/><text x="31" y="46" font-size="20" text-anchor="middle" fill="#fff" font-family="Arial" font-weight="700">$</text></svg>
    <h3>Workers'<br>Compensation</h3>
    <p>Lorem Ipsum is simply dummy... <span class="more">READ MORE</span></p>
  </div>
</section>

<section class="welcome">
  <div class="abs welcome-photo" role="img" aria-label="Two business colleagues in conversation"></div>
  <div class="abs welcome-text">
    <h2>WELCOME TO LARKFIELDHR</h2>
    <p>Lorem Ipsum is simply dummy text of the printing and typesetting industry. Lorem Ipsum has been the industry's standard dummy text ever since the 1500s, when an unknown printer took a galley of type and scrambled it to make a type specimen book. It has survived not only five centuries, but also the leap into electronic type setting, remaining essentially unchanged. It was popularised in the 1960s with...</p>
    <span class="btn-pill">READ MORE &#187;</span>
  </div>
</section>

<section class="broker">
  <h2 class="abs center section-title t-gold" style="top:52px">BROKER</h2>
  <p class="abs lead" style="left:200px;top:120px;width:800px;text-align:center">Lorem Ipsum is simply dummy text of the printing and typesetting industry. Lorem Ipsum has been the industry's standard dummy text ever since the 1500s.</p>
  <div class="abs broker-card" style="left:79px">
    <div class="ph" role="img" aria-label="Team meeting around a laptop" style="background:linear-gradient(135deg,#dfe3e8,#9aa7b6)"></div>
    <h3>orem Ipsum is simply dummy</h3>
    <p>Lorem Ipsum is simply dummy text<br>of the printing and typesetting industry.<br>Lorem Ipsum has... <span class="more">READ MORE</span> &#187;</p>
  </div>
  <div class="abs broker-card" style="left:439px">
    <div class="ph" role="img" aria-label="Presenter at a whiteboard in a meeting room" style="background:linear-gradient(135deg,#e8e8e6,#a9adb2)"></div>
    <h3>orem Ipsum is simply dummy</h3>
    <p>Lorem Ipsum is simply dummy text<br>of the printing and typesetting industry.<br>Lorem Ipsum has... <span class="more">READ MORE</span> &#187;</p>
  </div>
  <div class="abs broker-card" style="left:799px">
    <div class="ph" role="img" aria-label="Business people shaking hands" style="background:linear-gradient(135deg,#d8dde2,#7d8fa3)"></div>
    <h3>orem Ipsum is simply dummy</h3>
    <p>Lorem Ipsum is simply dummy text<br>of the printing and typesetting industry.<br>Lorem Ipsum has... <span class="more">READ MORE</span> &#187;</p>
  </div>
</section>

<section class="trust">
  <h2 class="abs center section-title t-blue" style="top:44px">Don't take our word for it!</h2>
  <p class="abs center lead" style="top:108px">We've been recognized and supported by the following organizations:</p>
  <div class="abs trust-logo" style="left:85px">LarkfieldHR</div>
  <div class="abs trust-logo" style="left:348px">LarkfieldHR</div>
  <div class="abs trust-logo" style="left:612px">LarkfieldHR</div>
  <div class="abs trust-logo" style="left:890px">LarkfieldHR</div>
</section>

<section class="resources">
  <h2 class="abs center section-title" style="top:52px;color:#fff">FEATURED RESOURCES</h2>
  <p class="abs" style="left:200px;top:120px;width:800px;text-align:center;font-size:13px;line-height:1.7;color:#f8efe1">Lorem Ipsum is simply dummy text of the printing and typesetting industry. Lorem Ipsum has been the industry's standard dummy text ever since the 1500s.</p>
  <div class="abs res" style="left:79px">
    <div class="ph" role="img" aria-label="Colleagues working together at a desk" style="background:linear-gradient(135deg,#eef0f2,#9ca9b8)"></div>
    <h3>Lorem Ipsum simply</h3>
    <p>Lorem Ipsum is simply dummy text of the printing and typeset industry... <span class="more">READ MORE</span> &#187;</p>
  </div>
  <div class="abs res" style="left:349px">
    <div class="ph" role="img" aria-label="Hands reviewing documents and charts" style="background:linear-gradient(135deg,#f1f1ef,#b4b6b8)"></div>
    <h3>Lorem Ipsum simply</h3>
    <p>Lorem Ipsum is simply dummy text of the printing and typeset industry... <span class="more">READ MORE</span> &#187;</p>
  </div>
  <div class="abs res" style="left:618px">
    <div class="ph" role="img" aria-label="Presentation with charts on a board" style="background:linear-gradient(135deg,#f4f4f4,#b9bec4)"></div>
    <h3>Lorem Ipsum simply</h3>
    <p>Lorem Ipsum is simply dummy text of the printing and typeset industry... <span class="more">READ MORE</span> &#187;</p>
  </div>
  <div class="abs res" style="left:890px">
    <div class="ph" role="img" aria-label="Business handshake over a table" style="background:linear-gradient(135deg,#e4e7ea,#8495a8)"></div>
    <h3>Lorem Ipsum simply</h3>
    <p>Lorem Ipsum is simply dummy text of the printing and typeset industry... <span class="more">READ MORE</span> &#187;</p>
  </div>
</section>

<section class="blog">
  <h2 class="abs center section-title" style="top:50px"><span class="t-blue">RECENT</span> <span class="t-gold">BLOG</span></h2>
  <div class="abs post-img" role="img" aria-label="Team discussing work at a laptop" style="left:79px;background:linear-gradient(135deg,#e6e9ec,#9aa6b3)"></div>
  <div class="abs post" style="left:319px">
    <h4>Lorem Ipsum is simply dummy</h4>
    <div class="date">&#128197; December 13, 2016</div>
    <p>Lorem Ipsum is simply dummy text of the printing and typesetting industry.</p>
  </div>
  <div class="abs post-img" role="img" aria-label="Colleagues smiling in a meeting" style="left:623px;background:linear-gradient(135deg,#ecebe8,#a9a59f)"></div>
  <div class="abs post" style="left:861px">
    <h4>Lorem Ipsum is simply dummy</h4>
    <div class="date">&#128197; December 13, 2016</div>
    <p>Lorem Ipsum is simply dummy text of the printing and typesetting industry.</p>
  </div>
</section>

<section class="testimonials" role="img" aria-label="Customer support agent with headset, blurred behind a blue overlay">
  <h2 class="abs center section-title" style="top:50px;color:#fff">WHAT OUR CLIENTS SAY</h2>
  <div class="abs quote-mark">&#8220;</div>
  <p class="abs t-text">Lorem Ipsum is simply dummy text of the printing and typesetting industry. Lorem Ipsum has been the industry's standard dummy text ever since the 1500s, when an unknown printer took a galley of type and scrambled it to make a type specimen book. It has survived not only five centuries, but also the leap into electronic type setting.</p>
  <div class="abs avatar" role="img" aria-label="Client portrait"></div>
  <div class="abs client">- CLIENT NAME</div>
  <div class="abs circle-arrow" style="left:79px"><svg width="32" height="32"><path d="M19 10l-6 6 6 6" fill="none" stroke="#fff" stroke-width="2"/></svg></div>
  <div class="abs circle-arrow" style="left:1088px"><svg width="32" height="32"><path d="M13 10l6 6-6 6" fill="none" stroke="#fff" stroke-width="2"/></svg></div>
</section>

<section class="contact">
  <h2 class="abs center section-title" style="top:44px"><span class="t-blue">TALK TO A</span> <span class="t-gold">TEAM MEMBER</span> <span class="t-blue">TODAY</span></h2>
  <div class="abs field" style="left:214px;top:136px">First Name</div>
  <div class="abs field" style="left:614px;top:136px">Last Name</div>
  <div class="abs field" style="left:214px;top:197px">Company</div>
  <div class="abs field" style="left:614px;top:197px">Phone</div>
  <div class="abs field" style="left:214px;top:258px">Email</div>
  <div class="abs submit">SUBMIT</div>
</section>

<footer class="site-footer">
  <div class="abs" style="left:79px;top:80px;font-size:30px;font-weight:700;color:var(--blue)">LarkfieldHR</div>
  <span class="abs foot-social" style="left:80px"></span>
  <span class="abs foot-social" style="left:151px"></span>
  <span class="abs foot-social" style="left:224px"></span>
  <h5 style="left:351px">Useful Links</h5>
  <div class="abs links">Home<br>About<br>Services<br>Broker<br>Resources<br>Blog<br>Contact</div>
  <h5 style="left:620px">Newsletter</h5>
  <div class="abs foot-input" style="top:90px">Enter Name</div>
  <div class="abs foot-input" style="top:152px">Enter Email</div>
  <div class="abs subscribe">SUBSCRIBE</div>
  <h5 style="left:890px">Get In Touch With Us</h5>
  <svg class="abs" style="left:890px;top:80px" width="16" height="20" viewBox="0 0 16 20"><path d="M8 0a7 7 0 0 1 7 7c0 5-7 13-7 13S1 12 1 7a7 7 0 0 1 7-7z" fill="#fff"/><circle cx="8" cy="7" r="2.5" fill="#5b5b5b"/></svg>
  <div class="abs contact-line" style="top:76px">Lorem Ipsum is simply dummy text of the printing and typesetting.</div>
  <svg class="abs" style="left:890px;top:149px" width="16" height="16" viewBox="0 0 16 16"><path d="M3 1c2 0 3 4 2 5l-1 1c1 2 3 4 5 5l1-1c1-1 5 0 5 2l-1 2C7 16 0 9 1 2z" fill="#fff"/></svg>
  <div class="abs contact-line" style="top:146px">123 456 7890</div>
  <svg class="abs" style="left:890px;top:182px" width="16" height="12" viewBox="0 0 16 12"><rect x="1" y="1" width="14" height="10" fill="none" stroke="#fff" stroke-width="1.5"/><path d="M1 1l7 6 7-6" fill="none" stroke="#fff" stroke-width="1.5"/></svg>
  <div class="abs contact-line" style="top:176px;color:#cfcfcf">Lorem Ipsum is simply</div>
  <svg class="abs" style="left:890px;top:210px" width="16" height="16" viewBox="0 0 16 16"><circle cx="8" cy="8" r="7" fill="none" stroke="#fff" stroke-width="1.5"/><path d="M1 8h14M8 1c-3 4-3 10 0 14M8 1c3 4 3 10 0 14" fill="none" stroke="#fff" stroke-width="1"/></svg>
  <div class="abs contact-line" style="top:206px;color:#cfcfcf">Lorem Ipsum is simply</div>
</footer>

<div class="bottom-bar" style="position:relative;width:1200px">
  <div class="abs" style="left:79px;top:11px">&#169; <b>LARKFIELDHR</b> - 2016. All Rights Reserved.</div>
  <div class="abs" style="left:872px;top:11px">Privacy policy</div>
  <div class="abs" style="left:990px;top:11px">|</div>
  <div class="abs" style="left:1016px;top:11px">Terms of Use</div>
</div>

</body>
</html>
```